Buchcover-Design für Ratgeber
Zielgruppe
Wir veröffentlichen Ebooks und Taschenbücher auf Lumora und benötigen für ein aktuelles Projekt noch ein Ebook Cover. Die Zielgruppe sind werdende und frisch gebackene Väter im Alter zwischen 25 und 40 Jahren.
Titel: KNIRPSOLOGIE, Vati kriegt das hin
Untertitel: Raus aus der Panik und rein ins Vater werden mit Verantwortung, Herz und Stil
Autor: Gernot Wallbrecht
Der Fokus des Buches richtet sich darauf, Vätern und denen, die es noch werden wollen, wertvolle Tipps und Handlungsempfehlungen mitzugeben, wie man sich als moderner, engagiertet Vater positioniert. Es richtet sich an Männer, die sich aktiv in die Erziehung ihres Kindes einbringen wollen und mehr sein wollen, als nur der Ernährer und Geldverdiener. Diese Zielgruppe ist bereit, Zeit zu investieren und sich darum zu bemühen, sich das Wissen anzueignen, wie sie ihre Partnerin während Schwangerschaft und Geburt unterstützen und wie sie eine starke Vater-Kind-Beziehung aufbauen können.
Das Hauptproblem dieser Zielgruppe ist, dass sie nur wenig Ahnung von Kindererziehung oder Schwangerschaft hat. Daher herrscht hier eine große Ratlosigkeit und Unsicherheit vor, da sie zum einen möglichst alles richtig machen will, zum Anderen aber nicht weiß, wie sie das anstellen und worauf alles zu achten ist.
Das Buch soll mit Cover und Titel die Botschaft senden, dass diese Sorgen unnötig sind und dass Daddy schon alles regelt. natürlich nur, wenn er das Buch gelesen hat ;-)
Aufgabenstellung
Wir hätten gerne ein Cover, welches ein kreatives Konzept abbildet und nicht nach Quobix-Standard bloß Titel, Stockfoto und den Namen des Autors darstellt. Ich denke es eignet sich hier mit dem Titel etwas auszuprobieren, da so ein Wortspiel wahrscheinlich einiges an kreativen Möglichkeiten bietet. Grundsätzlich sollten Cover, Titel und Untertitel miteinander harmonieren und ein schlüssiges Konzept darstellen, welches die Botschaft des Buches einfach rüber bringt.
Ansonsten haben wir keine weiteren Angaben wie Farben, Beispielcover usw. Hier könnt ihr kreativ werden!

```html
<!DOCTYPE html>
<html lang="de">
<head>
<meta charset="utf-8">
<title>KNIRPSOLOGIE – Vati kriegt das hin</title>
<link rel="stylesheet" href="https://fonts.googleapis.com/css2?family=Fredoka:wght@500;600&family=Dosis:wght@400;500&family=Allura&display=swap">
<style>
  :root {
    --bg: #ececec;
    --navy: #1b3159;
    --navy-band: rgba(30, 45, 88, 0.88);
    --sky: #94bbd7;
    --red: #c81d1d;
    --white: #ffffff;
    --bubble: #f4f6fa;
  }
  * { margin: 0; padding: 0; box-sizing: border-box; }
  html, body { width: 1200px; height: 794px; overflow: hidden; background: var(--bg); }
  .stage { position: relative; width: 1200px; height: 794px; }

  /* Front cover */
  .front-cover {
    position: absolute; left: 60px; top: 67px; width: 440px; height: 660px;
    overflow: hidden; box-shadow: 0 8px 24px rgba(0,0,0,0.18);
  }
  .cover-photo {
    position: absolute; inset: 0;
    background:
      radial-gradient(ellipse at 25% 40%, #f1d9c8 0%, rgba(241,217,200,0) 30%),
      radial-gradient(ellipse at 20% 18%, #9ba3ae 0%, rgba(155,163,174,0) 32%),
      radial-gradient(ellipse at 80% 45%, #d39a78 0%, rgba(211,154,120,0) 28%),
      radial-gradient(ellipse at 78% 75%, #2d3f68 0%, rgba(45,63,104,0) 45%),
      linear-gradient(170deg, #8fb3d6 0%, #b8c3cf 35%, #7d8aa0 60%, #6b4b35 100%);
  }
  .bubble { position: absolute; }
  .bubble svg { position: absolute; inset: 0; width: 100%; height: 100%; overflow: visible; }
  .bubble-top { left: 118px; top: 10px; width: 300px; height: 250px; }
  .bubble-top .bubble-text {
    position: absolute; left: 40px; top: 38px; width: 250px;
    transform: rotate(-14deg); transform-origin: center; text-align: center;
  }
  .word-tail {
    display: block; font-family: "Fredoka", sans-serif; font-weight: 500;
    font-size: 58px; line-height: 1; color: var(--navy); letter-spacing: -1px;
  }
  .tagline {
    display: block; font-family: "Fredoka", sans-serif; font-weight: 600;
    font-size: 30px; line-height: 1.05; color: var(--red); margin-top: 4px;
  }
  .bubble-bottom { left: 58px; top: 360px; width: 220px; height: 170px; }
  .bubble-bottom .word-head {
    position: absolute; left: 18px; top: 62px; transform: rotate(-9deg);
    font-family: "Fredoka", sans-serif; font-weight: 500; font-size: 44px;
    color: var(--navy); letter-spacing: -1px; white-space: nowrap;
  }
  .subtitle-band {
    position: absolute; left: 96px; right: 0; top: 565px; padding: 6px 14px 6px 10px;
    background: var(--navy-band); color: var(--white); text-align: right;
    font-family: "Dosis", sans-serif; font-weight: 500; font-size: 15.5px; line-height: 1.3;
  }
  .author-front {
    position: absolute; right: 14px; bottom: 14px; color: var(--white);
    font-family: "Dosis", sans-serif; font-weight: 500; font-size: 15px; letter-spacing: 0.3px;
  }

  /* Back cover */
  .back-cover {
    position: absolute; left: 620px; top: 67px; width: 440px; height: 660px;
    background: var(--sky); box-shadow: 0 8px 24px rgba(0,0,0,0.14);
  }
  .text-panel {
    position: absolute; left: 75px; top: 50px; width: 270px; height: 470px;
    background: var(--navy);
  }
  .author-photo {
    position: absolute; left: 16px; top: 44px; width: 136px; height: 186px;
    background:
      radial-gradient(ellipse at 50% 82%, #4e5763 0%, rgba(78,87,99,0) 55%),
      linear-gradient(160deg, #e6e4e0 0%, #cfcac4 55%, #6f7682 100%);
  }
  .blurb {
    position: absolute; color: var(--white); font-family: "Dosis", sans-serif;
    font-weight: 400; font-size: 10px; line-height: 1.42; text-align: justify; hyphens: manual;
  }
  .blurb-first { left: 160px; top: 90px; width: 178px; }
  .blurb-rest { left: 84px; top: 252px; width: 254px; }
  .blurb-rest p + p { margin-top: 10px; }
  .signature {
    position: absolute; left: 180px; top: 470px; color: var(--white);
    font-family: "Allura", cursive; font-size: 26px; white-space: nowrap;
  }

  /* Spine */
  .spine {
    position: absolute; left: 1060px; top: 67px; width: 40px; height: 660px;
    background: var(--navy); display: flex; align-items: center; justify-content: center;
  }
  .spine-title {
    writing-mode: vertical-rl; transform: rotate(180deg); white-space: nowrap;
    font-family: "Fredoka", sans-serif; font-weight: 500; font-size: 22px;
  }
  .spine-title .main { color: var(--white); }
  .spine-title .claim { color: var(--red); font-weight: 600; font-size: 19px; margin-left: 16px; }
</style>
</head>
<body>
<main class="stage">

  <section class="front-cover">
    <div class="cover-photo" role="img" aria-label="Foto: Baby mit grauer Mütze hält die Hand seines Vaters"></div>

    <div class="bubble bubble-top">
      <svg viewBox="0 0 300 250" aria-hidden="true">
        <path d="M20 120 Q10 80 50 66 L240 12 Q285 2 292 45 L298 150 Q300 185 262 194 L150 222 L140 252 L112 228 L70 236 Q40 240 34 205 Z"
              fill="var(--bubble)" stroke="var(--navy)" stroke-width="7" stroke-linejoin="round"/>
      </svg>
      <div class="bubble-text">
        <span class="word-tail">...ologie</span>
        <span class="tagline">Vati kriegt<br>das hin!</span>
      </div>
    </div>

    <div class="bubble bubble-bottom">
      <svg viewBox="0 0 220 170" aria-hidden="true">
        <path d="M8 70 Q4 48 28 44 L52 40 L60 8 L82 30 L160 18 Q182 14 190 34 L214 118 Q220 140 196 146 L44 168 Q22 170 20 148 Z"
              fill="var(--bubble)" stroke="var(--navy)" stroke-width="6" stroke-linejoin="round"/>
      </svg>
      <span class="word-head">KNIRPS...</span>
    </div>

    <p class="subtitle-band">Raus aus der Panik und rein ins Vater werden<br>mit Verantwortung, Herz und Stil</p>
    <p class="author-front">Gernot Wallbrecht</p>
  </section>

  <section class="back-cover">
    <div class="text-panel"></div>
    <div class="author-photo" role="img" aria-label="Porträtfoto des Autors im grauen Strickpullover"></div>

    <p class="blurb blurb-first">Der Fokus des Buches richtet sich darauf, Vätern und denen, die es noch werden wollen, wertvolle Tipps und Handlungsempfehlun­gen mitzugeben, wie man sich als moderner, engagiertet Vater posi­tioniert. Es richtet sich an Männer, die sich aktiv in die Erziehung ihres Kindes einbringen wollen und mehr sein wollen, als nur der Ernährer und Geldverdienner.</p>

    <div class="blurb blurb-rest">
      <p>Diese Zielgruppe ist bereit, Zeit zu investieren und sich darum zu bemühen, sich das Wissen anzueig­nen, wie sie ihre Partnerin während Schwanger­schaft und Geburt unterstützen und wie sie eine starke Vater-Kind-Beziehung aufbauen können.</p>
      <p>Das Hauptproblem dieser Zielgruppe ist, dass sie nur wenig Ahnung von Kindererziehung oder Schwangerschaft hat. Daher herrscht hier eine große Ratlosigkeit und Unsicherheit vor, da sie zum einen möglichst alles richtig machen will, zum Anderen aber nicht weiß, wie sie das anstellen und worauf alles zu achten ist.</p>
    </div>

    <p class="signature">Gernot Wallbrecht</p>
  </section>

  <aside class="spine">
    <p class="spine-title"><span class="main">KNIRPSologie</span><span class="claim">Vati kriegt das hin!</span></p>
  </aside>

</main>
</body>
</html>
```